Business Card Design Project

We need a business card for a new technology services company. We develop software and implement software packages for our business customers and although we will begin with just one or two service offerings, our service offerings will expand over time. Our name comes from the an author, RK Linford, and his "idea" was that opportunity should be based on ability and achievement, not on social status.

We would like to see a design that is standard in its size and shape, but stands apart in its dramatic color contrasts. The card should not use too many colors - the colors used in the background should highlight the brilliant blues of the logo (see attachment) to dramatic effect. The background should not be white.

If necessary, you can change the color of the words "RK Linford", but not the word "Notion".

Card size should be U.S. standard 2 inches by 3.5 inches and provide for 1/8 inch bleed area on each side.

We need a design for both sides of the business card, one side communicating the company logo and contact information, the other side being purely graphical, incorporating the logo but no other information.

Contact Information Required:
Mark Pell
MarkPell@rklinfordnotion.example
555-384-9172

Target Market(s)

Business executives

Industry/Entity Type

Software

Requirements
Must have
• It must have the full company logo on one side, and at least the graphic element of the logo on the other. Either that or the full logo on both.
Nice to have
• It would be nice to have a design that could work without needing two different textures. For example, it would be nice if the entire card could be shiny, not just parts of the card.

It would also be nice if texture is something we could add later.
Should not have
• The card should not use the color green.

```html
<!DOCTYPE html>
<html lang="en">
<head>
<meta charset="utf-8">
<title>RK Linford Notion – Business Card</title>
<link rel="stylesheet" href="https://fonts.googleapis.com/css2?family=Roboto:wght@300&family=Hind:wght@500&family=Crimson+Text:ital,wght@1,700&display=swap">
<style>
  :root {
    --stage: #cccafc;
    --card-black: #0a0b0d;
    --accent-cyan: #00c8e6;
    --panel-light: #e7ecec;
    --wordmark-grey: #a9abae;
    --ink-dark: #0d0d10;
  }
  html, body {
    margin: 0;
    padding: 0;
    width: 1200px;
    height: 405px;
    overflow: hidden;
    background: var(--stage);
  }
  .stage {
    position: relative;
    width: 1200px;
    height: 405px;
  }
  .card {
    position: absolute;
    top: 61px;
    width: 495px;
    height: 283px;
    overflow: hidden;
    background: var(--card-black);
  }
  .card--front { left: 95px; border-radius: 28px; }
  .card--back  { left: 609px; border-radius: 40px; }
  .card__shapes {
    position: absolute;
    inset: 0;
  }
  .wordmark {
    position: absolute;
    margin: 0;
    font-family: "Roboto", Arial, sans-serif;
    font-weight: 300;
    color: var(--wordmark-grey);
    letter-spacing: -1px;
    white-space: nowrap;
    line-height: 1;
  }
  .card--front .wordmark { left: 42px; top: 101px; font-size: 40px; }
  .card--back .wordmark  { left: 74px; top: 120px; font-size: 36px; }
  .holder-name {
    position: absolute;
    left: 0;
    right: 0;
    top: 184px;
    margin: 0;
    line-height: 1.2;
    text-align: center;
    font-family: "Hind", Arial, sans-serif;
    font-weight: 500;
    font-size: 21px;
    color: var(--accent-cyan);
  }
  .contact {
    position: absolute;
    top: 259px;
    margin: 0;
    line-height: 18px;
    display: flex;
    align-items: center;
    gap: 5px;
    white-space: nowrap;
    font-family: "Crimson Text", Georgia, serif;
    font-style: italic;
    font-weight: 700;
    font-size: 13.5px;
    color: var(--ink-dark);
  }
  .contact--email { left: 36px; }
  .contact--phone { right: 34px; }
  .contact__icon { width: 15px; height: 15px; fill: var(--accent-cyan); flex: none; }
</style>
</head>
<body>
<main class="stage">

  <section class="card card--front" aria-label="Business card front">
    <svg class="card__shapes" viewBox="0 0 495 283" aria-hidden="true">
      <path d="M0 283 V210 Q247 140 495 210 V283 Z" fill="var(--panel-light)"/>
      <rect x="0" y="0" width="26" height="283" fill="var(--accent-cyan)"/>
      <rect x="469" y="0" width="26" height="283" fill="var(--accent-cyan)"/>
      <circle cx="398" cy="68" r="28" fill="var(--accent-cyan)"/>
    </svg>
    <p class="wordmark">RK Linford Notion</p>
    <p class="holder-name">Mark Pell</p>
    <p class="contact contact--email">
      <svg class="contact__icon" viewBox="0 0 24 24" aria-hidden="true"><path d="M12 2a10 10 0 1 0 5 18.7l-1-1.7A8 8 0 1 1 20 12v1.2a1.8 1.8 0 0 1-3.6 0V7.5h-2v.9A5 5 0 1 0 15 16a3.8 3.8 0 0 0 7-2.8V12A10 10 0 0 0 12 2Zm0 13a3 3 0 1 1 0-6 3 3 0 0 1 0 6Z"/></svg>
      MarkPell@rklinfordnotion.example
    </p>
    <p class="contact contact--phone">
      <svg class="contact__icon" viewBox="0 0 24 24" aria-hidden="true"><path d="M7 2 9.5 7 7.8 8.6c.9 2.9 2.6 5.4 5 7.3L14.6 14.5 19 17.5 17 21C10 20 4 13 3.5 5Z"/></svg>
      555-384-9172
    </p>
  </section>

  <section class="card card--back" aria-label="Business card back">
    <svg class="card__shapes" viewBox="0 0 495 283" aria-hidden="true">
      <defs>
        <linearGradient id="horizon-sheen" x1="0" y1="0" x2="0" y2="1">
          <stop offset="0" stop-color="#1a1b1e"/>
          <stop offset="0.25" stop-color="#020203"/>
          <stop offset="1" stop-color="#000"/>
        </linearGradient>
      </defs>
      <path d="M0 283 V220 Q247 170 495 220 V283 Z" fill="url(#horizon-sheen)"/>
      <circle cx="372" cy="96" r="25" fill="var(--accent-cyan)"/>
    </svg>
    <p class="wordmark">RK Linford Notion</p>
  </section>

</main>
</body>
</html>
```